Personal Development company in need for a fun website

KV7 effectively encourages personal growth and self-improvement by providing the positive tools which will motivate, enlighten and empower the client in a relaxed, friendly environment. Taking care of the ‘self’ is essential to being productive and valuable in all aspects of life, professionally and personally. We want it to be edgy and fun targeting professionals, youth and women entering the workforce.

We would need a homepage that would have a news and features, an online shop for some of our products, a schedule for our events and workshops, a calendar, an about us section and team. Other features that need to be added terms and conditions, privacy, link to social media on the bottom of the home page.

Please look at brain dock and the hall of dawns to understand our concept.

Target Market(s)

Young professionals, women that want to enter the workplace, individuals of all ages seeking personal development in all its forms.

Industry/Entity Type

It Company

Coding

Coded - Design and coding required

Number of Pages Required

5+ page

Font styles to use
Sans Serif

Requirements
Must have
• Must be clean and attractive.
Nice to have
• Graphic design work
Should not have
• Photographs, unless its the speaker of an event.

```html
<!DOCTYPE html>
<html lang="en">
<head>
<meta charset="utf-8">
<title>KV7 Growth Studio</title>
<link href="https://fonts.googleapis.com/css2?family=Quicksand:wght@400;500;700&family=Lato:wght@400;700&display=swap" rel="stylesheet">
<style>
:root{
  --red:#c8323f;
  --navy:#2b3990;
  --ink:#2a2a2a;
  --muted:#666;
  --line:#dcdcdc;
  --pale:#f1f1f3;
  --white:#fff;
}
*{box-sizing:border-box;margin:0;padding:0}
html,body{width:741px;height:1200px;overflow:hidden;background:var(--white)}
body{position:relative;font-family:'Lato',sans-serif;color:var(--ink)}
h1,h2,h3,.nav a,.brand{font-family:'Quicksand',sans-serif;font-weight:500}
.accent{color:var(--red)}

/* sidebar */
.sidebar{position:absolute;left:0;top:0;width:173px;height:1173px;border-right:1px solid var(--navy);background:var(--white)}
.brand{height:61px;display:flex;align-items:center;gap:7px;padding-left:7px;color:var(--red);font-size:15px;font-weight:700}
.brand-mark{width:22px;height:22px;background:var(--red)}
.nav{list-style:none}
.nav li{height:24.3px;border-bottom:1px solid var(--line)}
.nav a{display:flex;justify-content:space-between;align-items:center;height:100%;padding:0 10px 0 6px;font-size:10px;color:var(--navy);text-decoration:none}
.nav li.active{background:var(--red);border-color:var(--red)}
.nav li.active a{color:var(--white)}
.nav svg{width:13px;height:13px}
.newsletter{padding:22px 6px 0}
.newsletter h3{font-size:12px;color:var(--ink)}
.newsletter p{font-size:7.5px;color:var(--muted);margin-top:6px;line-height:1.4;width:140px}
.field{margin-top:8px;height:19px;border:1px solid var(--line);font-size:6.5px;font-style:italic;color:#888;padding:5px 7px}
.btn-navy{display:inline-block;background:var(--navy);color:var(--white);font-size:8px;font-weight:700;padding:5px 9px;margin-top:8px}
.follow{position:absolute;top:368px;left:0;right:0;border-top:1px solid var(--line);padding:17px 6px 0;display:flex;align-items:center;gap:8px}
.follow span{font-size:11px;font-style:italic;margin-right:2px}
.social{width:12px;height:12px;background:#3a3a3a}

/* main */
.main{position:absolute;left:174px;top:0;width:567px}
.hero{height:211px;position:relative;background:linear-gradient(120deg,#8fa2ad 0%,#c7d3d9 55%,#e2e9ec 100%)}
.hero h1{position:absolute;left:30px;top:40px;width:400px;font-size:16px;line-height:21px;font-weight:700;color:var(--white);text-shadow:0 1px 3px rgba(0,0,0,.45)}
.join{position:absolute;right:0;top:0;background:var(--navy);color:var(--white);font-size:8px;font-style:italic;font-weight:700;padding:3px 8px}
.dots{position:absolute;left:414px;top:194px;display:flex;gap:5px}
.dots i{width:32px;height:2px;background:#9aa6ac}
.dots i.on{background:var(--red)}

.welcome{height:173px;background:var(--pale);padding:22px 12px 0 12px}
.welcome h2{font-size:18px;color:var(--ink)}
.welcome p{font-size:8.2px;line-height:13.5px;color:#444;margin-top:10px;width:510px}
.welcome .btn-navy{margin-top:12px;font-weight:400;font-size:8.5px;padding:4px 9px}

.news{height:280px;padding:21px 12px 0 12px}
h2.section{font-size:17px;color:var(--ink)}
.cards{display:flex;gap:14px;margin-top:13px}
.card{width:160px;height:205px;border:1px solid var(--line);padding:6px}
.thumb{height:78px}
.card h3{font-size:11.5px;line-height:13.5px;color:var(--red);margin-top:9px}
.card p{font-size:7.6px;line-height:13.5px;color:#444;margin-top:7px}
.card .btn-navy{font-weight:400;font-size:8.5px;padding:4px 9px;margin-top:7px}

.features{height:176px;background:var(--pale);padding:22px 12px 0 12px;display:flex;gap:14px}
.tile{width:161px;height:133px;position:relative;text-align:center;color:var(--white)}
.tile h3{font-size:13.5px;padding-top:28px;font-weight:500}
.tile p{font-size:7.6px;line-height:13px;margin:6px auto 0;width:110px}
.tile .btn-red{display:inline-block;background:var(--red);font-size:8px;padding:4px 11px;margin-top:8px}

.team{height:232px;padding:28px 12px 0 12px}
.members{display:flex;gap:14px;margin-top:12px}
.member{width:162px}
.portrait{height:117px;border:1px solid var(--navy);background:linear-gradient(160deg,#bdbdbd,#5d5d5d)}
.member h3{font-size:12px;color:var(--red);margin-top:10px}
.member p{font-size:8.5px;margin-top:6px;padding-left:2px}

.contact{height:101px;background:var(--pale);padding:22px 12px 0 12px}
.contact-row{display:flex;margin-top:12px}
.item{display:flex;align-items:flex-start;gap:10px;font-size:8.8px;line-height:14px}
.item svg{width:22px;height:24px;flex:none}
.item.addr{width:170px}
.item.phone{width:120px}
.item.mail{font-size:8px}

.footer{position:absolute;left:0;top:1173px;width:741px;height:27px;background:var(--red);color:var(--white);font-size:8px;display:flex;justify-content:space-between;align-items:center;padding:0 46px 0 6px}
</style>
</head>
<body>

<aside class="sidebar">
  <div class="brand"><span class="brand-mark"></span>KV7 Growth Studio</div>
  <ul class="nav">
    <li class="active"><a href="#">Home<svg viewBox="0 0 16 16"><path d="M2 8 8 2l6 6M4 7v7h8V7" fill="none" stroke="#fff" stroke-width="2"/></svg></a></li>
    <li><a href="#">About Us<svg viewBox="0 0 16 16"><circle cx="9" cy="2.5" r="1.5" fill="#2b3990"/><path d="M8 6 6 15" stroke="#2b3990" stroke-width="2"/></svg></a></li>
    <li><a href="#">Insights<svg viewBox="0 0 16 16"><circle cx="8" cy="7" r="6" fill="#2b3990"/><rect x="5" y="11" width="5" height="4" fill="#2b3990"/></svg></a></li>
    <li><a href="#">Our Products<svg viewBox="0 0 16 16"><path d="M8 2 15 5 8 8 1 5Z" fill="#2b3990"/><path d="M1 8l7 3 7-3M1 11l7 3 7-3" fill="none" stroke="#2b3990" stroke-width="1.4"/></svg></a></li>
    <li><a href="#">Events &amp; Workshop<svg viewBox="0 0 16 16"><rect x="1" y="3" width="11" height="10" fill="none" stroke="#2b3990" stroke-width="1.4"/><path d="M1 6h11" stroke="#2b3990"/><circle cx="12" cy="12" r="3.5" fill="#fff" stroke="#2b3990"/></svg></a></li>
    <li><a href="#">Team<svg viewBox="0 0 16 16"><circle cx="4" cy="4" r="2" fill="#2b3990"/><circle cx="12" cy="4" r="2" fill="#2b3990"/><circle cx="8" cy="5" r="2" fill="#2b3990"/><rect x="2" y="7" width="4" height="7" fill="#2b3990"/><rect x="10" y="7" width="4" height="7" fill="#2b3990"/><rect x="6" y="8" width="4" height="7" fill="#2b3990"/></svg></a></li>
    <li><a href="#">Contact Us<svg viewBox="0 0 16 16"><path d="M3 3c3-2 7-2 10 0l-2 3H5Z" fill="#2b3990"/><rect x="3" y="7" width="10" height="7" rx="1" fill="none" stroke="#2b3990" stroke-width="1.4"/></svg></a></li>
  </ul>
  <div class="newsletter">
    <h3>Subscribe to Newsletter</h3>
    <p>Get Latest Updates By Entering Your Email Address</p>
    <div class="field">Email Address</div>
    <span class="btn-navy">Subscribe</span>
  </div>
  <div class="follow">
    <span>Follow Us</span>
    <i class="social" aria-label="Social link 1"></i>
    <i class="social" aria-label="Social link 2"></i>
    <i class="social" aria-label="Social link 3"></i>
    <i class="social" aria-label="Social link 4"></i>
  </div>
</aside>

<main class="main">
  <section class="hero" role="img" aria-label="Slide image: a red sphere leading a curved row of pale spheres up a white ramp">
    <span class="join">JOIN</span>
    <h1>We Effectively Encourage Personal Growth And Self-improvement By Providing The Positive Tools</h1>
    <div class="dots"><i class="on"></i><i></i><i></i></div>
  </section>

  <section class="welcome">
    <h2>Welcome To <span class="accent">KV7 Growth Studio</span></h2>
    <p>Lorem ipsum dolor sit amet, consectetuer adipiscing elit, sed diam nonummy nibh euismod tincidunt ut laoreet dolore magna aliquam eratLorem ipsum dolor sit amet, consectetuer adipiscing elit, sed diam nonummy nibh euismod tincidunt ut laoreet dolore magna aliquam erat volutpat. Ut wisi enim ad minim veniam, quis nostrud exerci tation ullamcorper suscipit lobortis nisl ut aliquip ex ea commodo consequat. Duis autem vel eum iriure dolor in hendrerit in vulputate velit esse molestie consequat, vel illum dolore eu feugiat nulla facilisis at vero eros et accumsan et iusto odio dignissim qui blandit praesent luptatum zzril delenit augue duis dolore te feugait nulla facilisi.</p>
    <span class="btn-navy">Read More</span>
  </section>

  <section class="news">
    <h2 class="section">Latest <span class="accent">News</span></h2>
    <div class="cards">
      <article class="card">
        <div class="thumb" role="img" aria-label="Photo of an open book in warm light" style="background:linear-gradient(180deg,#3a2414,#b67a3e 70%,#6a3f1e)"></div>
        <h3>Lorem ipsum dolor sit alm amet, consectetuer</h3>
        <p>Lorem ipsum dolor sit amet, almet sit consectetuer adipiscing elit, sed diam nonummy nibh euismod tincidunt..</p>
        <span class="btn-navy">Read More</span>
      </article>
      <article class="card">
        <div class="thumb" role="img" aria-label="Photo of a hiker on a mountain ridge at sunrise" style="background:linear-gradient(180deg,#c8d4dc,#e8d9b0 45%,#7c8160)"></div>
        <h3>Lorem ipsum dolor sit alm amet, consectetuer</h3>
        <p>Lorem ipsum dolor sit amet, almet sit consectetuer adipiscing elit, sed diam nonummy nibh euismod tincidunt..</p>
        <span class="btn-navy">Read More</span>
      </article>
      <article class="card">
        <div class="thumb" role="img" aria-label="Photo of open book pages in soft light" style="background:linear-gradient(180deg,#d9d9dc,#b9b5b3 60%,#6e625d)"></div>
        <h3>Lorem ipsum dolor sit alm amet, consectetuer</h3>
        <p>Lorem ipsum dolor sit amet, almet sit consectetuer adipiscing elit, sed diam nonummy nibh euismod tincidunt..</p>
        <span class="btn-navy">Read More</span>
      </article>
    </div>
  </section>

  <section class="features">
    <div class="tile" role="img" aria-label="Photo of a stack of old books" style="background:linear-gradient(160deg,#7a4a34,#4a2a20 60%,#2d2520)">
      <h3>Our Products</h3>
      <p>Lorem ipsum dolor sit amet, almet sit consectetuer</p>
      <span class="btn-red">Shop Now</span>
    </div>
    <div class="tile" role="img" aria-label="Photo of a workshop audience raising hands" style="background:linear-gradient(160deg,#4b4b4b,#2c2c2c 60%,#3d3230)">
      <h3>Events &amp; Workshops</h3>
      <p>Lorem ipsum dolor sit amet, almet sit consectetuer</p>
      <span class="btn-red">Enroll Now</span>
    </div>
    <div class="tile" role="img" aria-label="Photo of a calendar page with a red pin" style="background:linear-gradient(160deg,#3a3a3a,#1f1f1f 60%,#4a4a4a)">
      <h3>Event Calendar</h3>
      <p>Lorem ipsum dolor sit amet, almet sit consectetuer</p>
      <span class="btn-red">Read More</span>
    </div>
  </section>

  <section class="team">
    <h2 class="section">Our <span class="accent">Team</span></h2>
    <div class="members">
      <div class="member">
        <div class="portrait" role="img" aria-label="Black and white portrait of team member Owen Hartley"></div>
        <h3>Owen Hartley</h3>
        <p>Lorem ipsum dolor sit amet</p>
      </div>
      <div class="member">
        <div class="portrait" role="img" aria-label="Black and white portrait of team member Rory"></div>
        <h3>Rory</h3>
        <p>Lorem ipsum dolor</p>
      </div>
      <div class="member">
        <div class="portrait" role="img" aria-label="Black and white portrait of team member Liam Castell"></div>
        <h3>Liam Castell</h3>
        <p>Lorem ipsum dolor sit amet</p>
      </div>
    </div>
  </section>

  <section class="contact">
    <h2 class="section">Contact <span class="accent">Us</span></h2>
    <div class="contact-row">
      <div class="item addr">
        <svg viewBox="0 0 20 24"><path d="M10 1a8 8 0 0 0-8 8c0 6 8 14 8 14s8-8 8-14a8 8 0 0 0-8-8Z" fill="#2b3990"/><circle cx="10" cy="9" r="3" fill="#f1f1f3"/></svg>
        <span>Lorem ipsum dolor sit amet, consectetuer adipiscing</span>
      </div>
      <div class="item phone">
        <svg viewBox="0 0 24 24"><path d="M5 2l4 1 1 5-3 2c1 3 3 5 6 6l2-3 5 1 1 4c-1 3-4 4-7 3C8 19 4 14 2 8 1 5 2 3 5 2Z" fill="#2b3990"/></svg>
        <span>Phone<br>555-014-2283</span>
      </div>
      <div class="item mail">
        <svg viewBox="0 0 28 24"><path d="M2 10 14 2l12 8v12H2Z" fill="#2b3990"/><path d="M2 10l12 8 12-8" fill="none" stroke="#f1f1f3" stroke-width="1.5"/><path d="M9 9h10M9 12h10" stroke="#f1f1f3"/></svg>
        <span>Email<br>hello@kv7growthstudio.com</span>
      </div>
    </div>
  </section>
</main>

<footer class="footer">
  <span>© 2016 KV7 Growth Studio. All Rights Reserved.</span>
  <span>Privacy policy &nbsp;/&nbsp; Terms and conditions</span>
</footer>

</body>
</html>
```